Velorant Flyer

PROJECT: Digital Flyer for VeloRant

Format
1920 × 1080 px (landscape, optimized for presentations and email)
Deliverables
• PDF
• PNG

About VeloRant
VeloRant is a Dutch B2B software company providing a unified CRM and customer journey platform. We help businesses manage the entire customer lifecycle — from first contact to loyal customer — by centralizing all touchpoints in one system.
What sets us apart:
Extreme ease of use. The system is self-guiding, shows only what's relevant per employee, and requires virtually no training. All channels (email, phone, chat, in-store) come together in one place with automatic task distribution. Built-in AI functions as a smart digital colleague that continuously learns.
Target audience:
Directors and sales managers at B2B companies with multiple customer contact channels.

Goal:
We want to create a flyer that sets us apart from other CRM platform providers. Our aim is to achieve this through simplicity and a professional appearance. The design should reflect our core value: ease of use. The recipient should feel compelled to engage with us — not overwhelmed by information, but intrigued by clarity. Less is more.

Required Text Elements
Headline:
"CRM that adapts to how you work"
Subline:
"Discover how VeloRant simplifies your sales process"
Call-to-action:
"See it in action — book a call"
Contact details:
• hello@velorant.nl
• 023-5871469
• velorant.com

Required Visual Elements
• VeloRant logo (attached)

Design Style
• Modern / Minimalist
• Professional / Business
• Tech / Futuristic
• Clean with plenty of whitespace

Tone of voice:
Clear, positive and customer-focused. Practical and accessible business style aimed at communicating concrete value for users.

Design inspiration — please review these websites:
• orbitfen.com
• tavolo.app
• quillet.com
• norvadex.com
• plumbit.com
What We DON'T Want
• Bold / In-your-face
• Dense / Compact
• Trendy / Experimental
• Childlike / Cheerful
• Playful / Cartoonish
• Busy / Chaotic
Colors
Use the color palette from velorant.com (blues, whites, clean professional tones).
[Exact hex codes used for element on the website:
#344054;
#1a1b1f;
#0254ac
#002249;
#e5edf7;
background-color: #fff; ]
Competitors (for context only — do NOT copy)
• vendhaven.nl
• kelpnode.com
• marrowcrm.com
• tradewinder.com
Budget
$150
Deadline
January 26, 2026

```html
<!DOCTYPE html>
<html lang="en">
<head>
<meta charset="utf-8">
<title>VeloRant Flyer</title>
<link href="https://fonts.googleapis.com/css2?family=Inter:wght@400;600;700;800&display=swap" rel="stylesheet">
<style>
  :root {
    --page-bg: #18264a;
    --navy: #12235a;
    --sky: #169fdb;
    --ink: #2f3a4c;
    --soft-blue: #4f8ccb;
    --white: #ffffff;
    --mist: #f1f2f4;
    --icon: #c9d3e0;
  }
  * { box-sizing: border-box; margin: 0; padding: 0; }
  html, body {
    width: 1200px; height: 1200px; overflow: hidden;
    background: var(--page-bg);
    font-family: "Inter", Arial, sans-serif;
  }
  .flyer {
    position: absolute;
    left: 84px; top: 309px;
    width: 1032px; height: 581px;
    overflow: hidden;
    background:
      radial-gradient(ellipse 260px 200px at 100% 0%, rgba(79,140,203,0.95), rgba(79,140,203,0) 100%),
      radial-gradient(ellipse 480px 330px at 100% 0%, rgba(150,185,225,0.7), rgba(150,185,225,0) 100%),
      radial-gradient(ellipse 230px 190px at 0% 100%, rgba(79,140,203,0.95), rgba(79,140,203,0) 100%),
      radial-gradient(ellipse 380px 300px at 0% 100%, rgba(150,185,225,0.7), rgba(150,185,225,0) 100%),
      linear-gradient(135deg, var(--white) 0%, var(--mist) 40%, var(--mist) 70%, var(--white) 100%);
  }
  .flyer::before {
    content: "";
    position: absolute; inset: 0;
    background:
      linear-gradient(135deg, transparent 44%, rgba(255,255,255,0.75) 47%, transparent 50%),
      linear-gradient(135deg, transparent 58%, rgba(255,255,255,0.6) 61%, transparent 64%),
      linear-gradient(135deg, transparent 30%, rgba(255,255,255,0.5) 33%, transparent 36%);
  }
  .headline {
    position: absolute; left: 67px; top: 64px;
    font-size: 56px; font-weight: 800; letter-spacing: -0.01em;
    color: var(--navy); white-space: nowrap; line-height: 1;
  }
  .headline .accent { color: var(--sky); }
  .subline {
    position: absolute; left: 71px; top: 150px;
    padding-left: 17px;
    border-left: 2px solid var(--sky);
    font-size: 29px; font-weight: 700; line-height: 43px;
    color: var(--ink); letter-spacing: -0.005em;
  }
  .cta {
    position: absolute; left: 68px; top: 265px;
    width: 453px; height: 63px;
    border-radius: 32px;
    background: var(--white);
    box-shadow: 0 4px 10px rgba(18,35,90,0.12);
    display: flex; align-items: center; justify-content: center;
    font-size: 28px; font-weight: 700; color: var(--sky);
    letter-spacing: -0.01em; white-space: nowrap;
  }
  .contacts { position: absolute; left: 68px; top: 378px; list-style: none; }
  .contacts li {
    display: flex; align-items: center;
    height: 34px; margin-bottom: 17.5px;
    font-size: 27px; font-weight: 400; color: var(--ink);
  }
  .contacts svg { width: 22px; height: 22px; margin-right: 17px; flex: none; }
  .brand {
    position: absolute; left: 720px; top: 355px;
    width: 250px;
    display: flex; align-items: center; justify-content: center; gap: 14px;
  }
  .brand-dot { width: 40px; height: 40px; border-radius: 50%; background: var(--sky); }
  .brand-name { font-size: 44px; font-weight: 800; color: var(--navy); letter-spacing: -0.01em; }
</style>
</head>
<body>
  <main class="flyer">
    <h1 class="headline"><span class="accent">CRM</span> that adapts to how you work</h1>
    <p class="subline">Discover how VeloRant simplifies<br>your sales process</p>
    <div class="cta">See it in action — book a call</div>
    <ul class="contacts">
      <li>
        <svg viewBox="0 0 24 24" aria-hidden="true"><rect x="1.5" y="5" width="21" height="14" fill="none" stroke="var(--icon)" stroke-width="1.6"/><path d="M1.5 5 L12 13 L22.5 5 M1.5 19 L9 11.5 M22.5 19 L15 11.5" fill="none" stroke="var(--icon)" stroke-width="1.6"/></svg>
        hello@velorant.nl
      </li>
      <li>
        <svg viewBox="0 0 24 24" aria-hidden="true"><path d="M6 2.5 L9 6.5 L7.2 9 C8.4 11.8 10.6 14.2 13.5 15.6 L16 13.8 L20 16.8 L18 20.5 C10 20 3.5 13 3.3 5 Z" fill="none" stroke="var(--icon)" stroke-width="1.6" stroke-linejoin="round"/><path d="M13 3.5 A7 7 0 0 1 20 10.5 M13 7 A3.5 3.5 0 0 1 16.5 10.5" fill="none" stroke="var(--icon)" stroke-width="1.6"/></svg>
        023-5871469
      </li>
      <li>
        <svg viewBox="0 0 24 24" aria-hidden="true"><circle cx="12" cy="12" r="10" fill="none" stroke="var(--icon)" stroke-width="1.6"/><ellipse cx="12" cy="12" rx="4.5" ry="10" fill="none" stroke="var(--icon)" stroke-width="1.6"/><path d="M2 12 H22 M4 7 H20 M4 17 H20" stroke="var(--icon)" stroke-width="1.6"/></svg>
        velorant.com
      </li>
    </ul>
    <div class="brand">
      <span class="brand-dot"></span>
      <span class="brand-name">VeloRant</span>
    </div>
  </main>
</body>
</html>
```